winery and bed & breakfast business card

need a business card design
font and style same as our marketing material
also need something for letterhead

not too colorful, we want professional and simple
name
address
phone number
web site
email
Corvelli Vineyard believes raising a family, living and working passionately with wine on the East End is a privilege. They consider the greatest accolades received over the years have been the thousands of satisfied tasting room visitors. Enlightening visitors to their products and wine region are the most important reasons they continue to make wine on the North Fork
We have created a casual and cozy environment within a rustic historic barn.
An outside seating area nestled among the vines provides visitors with unforgettable sunset views as they enjoy Corvelli’s quality crafted wines.

Target Market(s)

adults over 21

Font styles to use
Serif

Colors
6b449b
ffc214
f78f20
ffffff

Requirements
Must have
• logo
• same font as attached
• logo colors

```html
<!DOCTYPE html>
<html lang="en">
<head>
<meta charset="utf-8">
<title>Corvelli Vineyard – Stationery</title>
<link href="https://fonts.googleapis.com/css2?family=Cinzel:wght@600&family=Tinos&family=Raleway:wght@400;500&display=swap" rel="stylesheet">
<style>
  :root {
    --plum: #4a2d52;
    --orange: #f39322;
    --ink: #555058;
    --paper: #ffffff;
    --watermark: #ebebeb;
    --backdrop: #ffffff;
  }
  * { margin: 0; padding: 0; box-sizing: border-box; }
  html, body { width: 900px; height: 1200px; overflow: hidden; background: var(--backdrop); }
  .canvas { position: relative; width: 900px; height: 1200px; }

  .sheet {
    position: absolute;
    background: var(--paper);
    box-shadow: 1px 2px 5px rgba(0,0,0,0.45);
  }

  .brand-mark { position: absolute; border-radius: 50%; background: var(--orange); }
  .brand-name {
    position: absolute;
    left: 0; right: 0;
    text-align: center;
    font-family: "Cinzel", serif;
    font-weight: 600;
    color: var(--plum);
    white-space: nowrap;
  }

  /* Business card – front */
  .card-front { left: 13px; top: 52px; width: 429px; height: 257px; }
  .card-front .brand-mark { left: 180px; top: 32px; width: 70px; height: 70px; }
  .card-front .brand-name { top: 114px; font-size: 16px; letter-spacing: 3px; }

  .holder { position: absolute; right: 235px; top: 166px; text-align: right; }
  .holder-name { font-family: "Tinos", serif; font-size: 18px; color: var(--ink); letter-spacing: 0.2px; }
  .holder-role { font-family: "Raleway", sans-serif; font-size: 13px; color: var(--ink); margin-top: 3px; }

  .divider { position: absolute; left: 214px; top: 167px; width: 2px; height: 60px; background: var(--plum); }

  .contact-list { position: absolute; left: 236px; top: 163px; list-style: none; }
  .contact-list li {
    display: flex; align-items: center; gap: 10px;
    height: 17px;
    font-family: "Raleway", sans-serif; font-size: 13px; color: var(--ink);
  }
  .contact-list svg { width: 13px; height: 13px; flex: none; }

  /* Business card – back */
  .card-back { left: 457px; top: 52px; width: 429px; height: 257px; }
  .card-back .brand-mark { left: 164px; top: 54px; width: 100px; height: 100px; }
  .card-back .brand-name { top: 168px; font-size: 24px; letter-spacing: 4px; }

  /* Letterhead */
  .letterhead { left: 142px; top: 347px; width: 648px; height: 836px; }
  .letterhead .brand-mark { left: 289px; top: 24px; width: 70px; height: 70px; }
  .letterhead .brand-name { top: 102px; font-size: 15px; letter-spacing: 2px; }
  .rule { position: absolute; height: 3px; background: var(--orange); }
  .rule-head-left { left: 0; width: 208px; top: 111px; }
  .rule-head-right { left: 440px; right: 0; top: 113px; }
  .rule-foot-left { left: 0; width: 226px; top: 778px; }
  .rule-foot-right { left: 424px; right: 0; top: 778px; }

  .watermark { position: absolute; left: 150px; top: 278px; width: 350px; height: 350px; border-radius: 50%; background: var(--watermark); }

  .footer-web {
    position: absolute; left: 0; right: 0; top: 768px; text-align: center;
    font-family: "Raleway", sans-serif; font-size: 16px; font-weight: 500; color: var(--ink);
  }
  .footer-address {
    position: absolute; left: 0; right: 0; top: 799px; text-align: center;
    font-family: "Raleway", sans-serif; font-size: 13px; color: var(--ink);
  }
</style>
</head>
<body>
<main class="canvas">

  <section class="sheet card-front" aria-label="Business card front">
    <div class="brand-mark"></div>
    <div class="brand-name">Corvelli Vineyard</div>

    <div class="holder">
      <div class="holder-name">NAME SURNAME</div>
      <div class="holder-role">Ocupation</div>
    </div>
    <div class="divider"></div>

    <ul class="contact-list">
      <li>
        <svg viewBox="0 0 16 16" aria-hidden="true"><path d="M2 8 L8 2.5 L14 8 M4 7 V14 H12 V7 M7 14 V10 H9 V14" fill="none" stroke="var(--orange)" stroke-width="1.6" stroke-linejoin="round"/></svg>
        address
      </li>
      <li>
        <svg viewBox="0 0 16 16" aria-hidden="true"><rect x="4.5" y="1.5" width="7" height="13" rx="1.5" fill="var(--orange)"/><rect x="6" y="3.5" width="4" height="6" fill="#fff"/><circle cx="8" cy="12.3" r="0.9" fill="#fff"/></svg>
        phone number
      </li>
      <li>
        <svg viewBox="0 0 16 16" aria-hidden="true"><circle cx="8" cy="8" r="6.3" fill="none" stroke="var(--orange)" stroke-width="1.5"/><ellipse cx="8" cy="8" rx="2.6" ry="6.3" fill="none" stroke="var(--orange)" stroke-width="1.2"/><path d="M1.8 8 H14.2 M3 4.8 H13 M3 11.2 H13" stroke="var(--orange)" stroke-width="1.1"/></svg>
        web site
      </li>
      <li>
        <svg viewBox="0 0 16 16" aria-hidden="true"><rect x="1.5" y="3.5" width="13" height="9" fill="none" stroke="var(--orange)" stroke-width="1.5"/><path d="M1.5 3.5 L8 9 L14.5 3.5" fill="none" stroke="var(--orange)" stroke-width="1.4"/></svg>
        email
      </li>
    </ul>
  </section>

  <section class="sheet card-back" aria-label="Business card back">
    <div class="brand-mark"></div>
    <div class="brand-name">Corvelli Vineyard</div>
  </section>

  <section class="sheet letterhead" aria-label="Letterhead">
    <div class="brand-mark"></div>
    <div class="brand-name">Corvelli Vineyard</div>
    <div class="rule rule-head-left"></div>
    <div class="rule rule-head-right"></div>

    <div class="watermark"></div>

    <div class="rule rule-foot-left"></div>
    <div class="rule rule-foot-right"></div>
    <div class="footer-web">www.website.com</div>
    <div class="footer-address">address linehere, street, city, country; phone number &nbsp;, email</div>
  </section>

</main>
</body>
</html>
```